Computer consultant website

Plivet Software is a newly started computer consulting company. It's a small one-man company that provides mostly Android applications but also websites in collaboration with designers. I'm running this company on the side of full time university studies.

I'm in need of a website which will function as:
Primarily - I'll direct potential clients to the page so they can read about the company, what i offer and past work.
Secondarily - Making my company visible through the web and maybe getting new clients.

The final design should look modern, clean and professional.

Pages that will be in the final website are (Note that it's not the exact titles as the page will not be in english):
* About
* Services (what Plivet offers)
* Portfolio/work
* Short news (like Framolines "News and press")
* Contact.

Inspiration
http://www.framoline.example/design/87836
http://www.quarnbelt.example/
http://www.framoline.example/design/845881
http://www.framoline.example/design/1369424 - Lighter design, however a bit cluttered.

No programming code is needed delivered at all. Focus on designing rather then coding.

If you have any questions, do not hesitate to send me a message.

Target Market(s)

Non-technical entrepreneurs and small companies.

Industry/Entity Type

University

Requirements
Must have
• Must have my company logo (see attachment).

Must in any way use both colors from my logo.

A way to logically rearrange content to fit smaller screens. I will implement this design so that it can be pleasantly viewed on mobile devices. You don't necessarily need to provide exactly how the design would look on mobile devices.

I need the following types of page designs:
* Landing page
* Content page
* Portfolio/work (with accompanying inside/clicked) page

Landing/start page must in any way include at least the information:
* Shorter version of "About Plivet"
* At least 1 most recent portfolio/work entry
* At least 1 most recent news entry
* Services that Plivet offers.
Nice to have
• -
Should not have
• Testimonials or newsletter.

```html
<!DOCTYPE html>
<html lang="en">
<head>
<meta charset="utf-8">
<title>Plivet Software</title>
<link rel="stylesheet" href="https://fonts.googleapis.com/css2?family=Oswald:wght@400;500;700&family=Yanone+Kaffeesatz:wght@300;400&family=Open+Sans:wght@400;600&family=Bree+Serif&family=Lora:wght@400;700&display=swap">
<style>
:root{
  --blue:#2a7ef0;
  --navy:#0f3f8f;
  --ink:#2f2f2f;
  --text:#777;
  --grey-head:#6e6e6e;
  --panel:#f6f6f6;
  --line:#dcdcdc;
  --footer:#222;
  --white:#fff;
}
*{margin:0;padding:0;box-sizing:border-box}
html,body{width:799px;height:1200px;overflow:hidden}
body{position:relative;background:var(--white);font-family:"Open Sans",Arial,sans-serif;color:var(--text)}
.abs{position:absolute}

/* header */
.site-header{position:absolute;left:0;top:0;width:799px;height:86px;background:linear-gradient(#fff,#e4e4e4);border-bottom:1px solid #cfcfcf}
.brand{position:absolute;left:93px;top:15px;display:flex;align-items:center;gap:10px}
.brand-dot{width:50px;height:50px;border-radius:50%;background:var(--blue)}
.brand-name{font-family:"Open Sans",sans-serif;font-weight:600;font-size:38px;color:var(--ink);letter-spacing:-1px}
.call{position:absolute;right:101px;top:8px;text-align:right;font-family:Oswald,sans-serif;line-height:26px}
.call-label{font-size:16px;color:var(--ink);font-weight:500}
.call-number{font-size:21px;color:var(--blue);font-weight:500;margin-left:8px}
.call-mail{font-family:Arial,sans-serif;font-size:8px;color:#333;line-height:10px}
.call-mail span{color:var(--blue)}
.main-nav{position:absolute;right:97px;top:62px;display:flex;font-family:"Open Sans",sans-serif;font-size:10.5px;color:var(--ink)}
.main-nav span{padding:0 8px;border-left:1px solid #bbb;line-height:16px}
.main-nav span:first-child{border-left:none}
.main-nav span:last-child{padding-right:0}

/* hero */
.hero{position:absolute;left:0;top:86px;width:799px;height:297px;background:var(--navy)}
.hero-copy{position:absolute;left:93px;top:104px;width:166px;height:260px;background:var(--blue);color:var(--white);padding:22px 7px}
.hero-title{font-family:Oswald,sans-serif;font-weight:700;font-size:25px;line-height:25px}
.hero-text{font-size:10.5px;line-height:15.5px;margin-top:18px}
.hero-more{position:absolute;left:8px;bottom:16px;font-size:9.5px;display:flex;align-items:center;gap:4px}
.hero-more i{width:10px;height:10px;background:rgba(255,255,255,.35)}
.hero-photo{position:absolute;left:259px;top:104px;width:443px;height:260px;background:linear-gradient(90deg,#9aa6b4,#c4cbd3 35%,#8f9aa8 70%,#b7c0ca)}

/* welcome */
.section-title{font-family:"Yanone Kaffeesatz",sans-serif;font-weight:300;font-size:21px;color:var(--blue)}
.welcome{left:93px;top:404px;width:218px}
.welcome p{font-size:9.5px;line-height:14.5px;margin-top:10px}

/* services */
.services{left:330px;top:402px;width:180px;height:235px;background:var(--panel);border:1px solid #e4e4e4}
.box-head{height:33px;padding:4px 14px;font-family:"Yanone Kaffeesatz",sans-serif;font-weight:300;font-size:21px;color:var(--white)}
.services .box-head{background:var(--blue)}
.services ul{list-style:none;padding:2px 10px 0 12px}
.services li{font-size:9.5px;height:23.6px;line-height:23px;border-bottom:1px solid var(--line);color:#6a6a6a}
.services li:last-child{border:none}
.services li::before{content:"›";color:var(--blue);margin-right:6px;font-size:12px}

/* news */
.news{left:522px;top:402px;width:180px;height:235px;background:var(--panel);border:1px solid #e4e4e4}
.news .box-head{background:var(--grey-head)}
.news-item{padding:0 12px;margin-top:14px}
.news-date{font-size:7px;color:#999}
.news-title{font-size:9px;color:#222}
.news-text{font-size:7.5px;line-height:10px;color:#999;text-align:justify}

.divider{left:93px;top:652px;width:610px;height:12px;background:radial-gradient(ellipse at top,rgba(0,0,0,.1),transparent 70%)}

/* jobs */
.jobs-title{left:93px;top:678px;font-size:18px}
.job{position:absolute;top:710px;display:flex;gap:8px}
.job-photo{width:65px;height:65px;background:linear-gradient(#ececec,#c9c9c9);border:3px solid #eee}
.job-name{font-size:9.5px;color:#222}
.job-text{font-size:8px;line-height:11px;color:#888;margin-top:3px;width:76px}

/* footer */
.site-footer{position:absolute;left:0;top:828px;width:799px;height:372px;background:var(--footer);color:var(--white);text-align:center}
.social{position:absolute;top:17px;width:26px;height:26px;border-radius:50%;background:var(--blue)}
.foot-head{position:absolute;left:0;width:100%;font-family:Lora,serif;font-weight:700;font-size:10px;letter-spacing:.3px}
.contact-col{position:absolute;top:92px;width:300px;text-align:center}
.contact-lead{font-family:"Bree Serif",serif;font-size:18px;color:var(--blue);margin-top:4px}
.contact-value{font-family:Lora,serif;font-size:18px;margin-top:0}
.tweet{position:absolute;left:110px;top:238px;width:580px;font-size:10.5px;line-height:13px;color:#bbb}
.tweet b{color:var(--white);font-weight:400}
.tweet-time{position:absolute;left:0;top:270px;width:100%;font-size:8px;color:#888}
.foot-dot{position:absolute;left:388px;top:295px;width:24px;height:24px;border-radius:50%;background:var(--blue)}
.foot-nav{position:absolute;top:331px;left:0;width:100%;display:flex;justify-content:center;gap:16px;font-size:7.8px;color:#ddd}
.copyright{position:absolute;top:347px;left:0;width:100%;font-size:7px;color:#999}
</style>
</head>
<body>

<header class="site-header">
  <div class="brand"><span class="brand-dot"></span><span class="brand-name">Plivet</span></div>
  <div class="call">
    <div><span class="call-label">CALL US NOW ON:</span><span class="call-number">1300 42 71 05</span></div>
    <div class="call-mail">or email us at <span>support@plivet.example</span></div>
  </div>
  <nav class="main-nav">
    <span>HOME</span><span>ABOUT</span><span>SERVICES</span><span>PORTFOLIO/WORK</span><span>SHORT NEWS</span><span>CONTACT</span>
  </nav>
</header>

<section class="hero"></section>
<div class="hero-copy">
  <h1 class="hero-title">LOREM IPSUM DOLOR SIT AMET</h1>
  <p class="hero-text">Lorem ipsum dolor sit amet, consectetur adipisicing elit, sed do eiusmod tempor incididunt ut labore et dolore magna aliqua.</p>
  <div class="hero-more"><i></i>Read more</div>
</div>
<div class="hero-photo" role="img" aria-label="Photo of a smiling businessman in a suit with colleagues in an office behind him"></div>

<section class="abs welcome">
  <h2 class="section-title">Welcome to Plivet</h2>
  <p>Lorem Ipsum. Proin gravida nibh vel velit auctor aliquet. Aenean sollicitudin, lorem quis bibendum auctor, nisi elit consequat ipsum, nec sagittis sem nibh id elit. Duis sed odio sit amet nibh vulputate cursus a sit amet mauris. Morbi accumsan ipsum velit. Nam nec tellus a odio tincidunt auctor a ornare odio. Sed non mauris vitae erat consequat auctor eu in elit. Class aptent taciti sociosqu ad litora torquent per</p>
  <p style="margin-top:18px">conubia nostra, per inceptos himenaeos. Mauris in erat justo. Nullam ac urna eu felis dapibus condimentum sit amet a augue.</p>
</section>

<section class="abs services">
  <h2 class="box-head">Our Services</h2>
  <ul>
    <li>Suspendisse egestas dui ac</li>
    <li>Proin id risus sed sem</li>
    <li>Sed non lectus orci</li>
    <li>Sed sit amet urna orci</li>
    <li>Suspendisse egestas dui ac</li>
    <li>Proin id risus sed sem</li>
    <li>Sed non lectus orci</li>
    <li>Sed sit amet urna orci</li>
  </ul>
</section>

<section class="abs news">
  <h2 class="box-head">News &amp; Events</h2>
  <div class="news-item"><div class="news-date">20 Oct 2012</div><div class="news-title">Lorem ipsum dolor sit amet</div><div class="news-text">Pellentesque pulvinar enim non turpis ultrices et vehicula erat.</div></div>
  <div class="news-item"><div class="news-date">20 Oct 2012</div><div class="news-title">Lorem ipsum dolor sit amet</div><div class="news-text">Pellentesque pulvinar enim non turpis ultrices et vehicula erat.</div></div>
  <div class="news-item"><div class="news-date">20 Oct 2012</div><div class="news-title">Lorem ipsum dolor sit amet</div><div class="news-text">Pellentesque pulvinar enim non turpis ultrices et vehicula erat.</div></div>
</section>

<div class="abs divider"></div>

<h2 class="abs section-title jobs-title">Latest Job</h2>
<div class="job" style="left:93px"><div class="job-photo" role="img" aria-label="Portrait photo of a team member"></div><div><div class="job-name">Lorem ipsum</div><div class="job-text">Maecenas sollicitudin lorem in orci element um nec semper.</div></div></div>
<div class="job" style="left:247px"><div class="job-photo" role="img" aria-label="Portrait photo of a team member"></div><div><div class="job-name">Lorem ipsum</div><div class="job-text">Maecenas sollicitudin lorem in orci element um nec semper.</div></div></div>
<div class="job" style="left:402px"><div class="job-photo" role="img" aria-label="Portrait photo of a team member"></div><div><div class="job-name">Lorem ipsum</div><div class="job-text">Maecenas sollicitudin lorem in orci element um nec semper.</div></div></div>
<div class="job" style="left:562px"><div class="job-photo" role="img" aria-label="Portrait photo of a team member"></div><div><div class="job-name">Lorem ipsum</div><div class="job-text">Maecenas sollicitudin lorem in orci element um nec semper.</div></div></div>

<footer class="site-footer">
  <span class="social" style="left:318px"></span>
  <span class="social" style="left:385px"></span>
  <span class="social" style="left:446px"></span>

  <div class="foot-head" style="top:65px">HELP &amp; SUPPORT</div>

  <div class="contact-col" style="left:89px">
    <svg width="26" height="30" viewBox="0 0 24 24" aria-hidden="true"><path fill="#fff" d="M6.6 10.8a15 15 0 0 0 6.6 6.6l2.2-2.2a1 1 0 0 1 1-.25 11.4 11.4 0 0 0 3.6.57 1 1 0 0 1 1 1V20a1 1 0 0 1-1 1A17 17 0 0 1 3 4a1 1 0 0 1 1-1h3.5a1 1 0 0 1 1 1c0 1.25.2 2.45.57 3.57a1 1 0 0 1-.25 1z"/></svg>
    <div class="contact-lead">Need more info? Call us now!</div>
    <div class="contact-value">1300 42 71 05</div>
  </div>
  <div class="contact-col" style="left:398px">
    <svg width="28" height="22" viewBox="0 0 28 22" aria-hidden="true" style="margin-top:6px"><rect x="1" y="1" width="26" height="20" fill="none" stroke="#fff" stroke-width="2"/><path d="M1 1l13 11L27 1M1 21l10-10M27 21L17 11" fill="none" stroke="#fff" stroke-width="2"/></svg>
    <div class="contact-lead">Email</div>
    <div class="contact-value">support@plivet.example</div>
  </div>

  <div class="foot-head" style="top:196px">FOLLOW US ON CHIRPLINE</div>
  <p class="tweet">@nox Proin non reos mauris, in suscipit nisl. Mauris <b>http://lorvane.example/sollicitudin</b> sem but I must explain to you how all this mistaken idea of denouncing</p>
  <div class="tweet-time">2 hours ago</div>

  <span class="foot-dot"></span>
  <nav class="foot-nav"><span>HOME</span><span>ABOUT</span><span>SERVICES</span><span>PORTFOLIO/WORK</span><span>SHORT NEWS</span><span>CONTACT</span></nav>
  <div class="copyright">© Plivet 2013</div>
</footer>

</body>
</html>
```